Webdesign für Beratung zu Themen der Qualität und Nachhaltigkeit
Zielgruppe
Ich werde mich ab 1.1.23 selbständig machen mit der Beratung zu Themen der Qualität und Nachhaltigkeit. Meine Zielgruppe sind Bildungsinstitutionen, insbesondere Volkshochschulen.
Die Webseite richtet sich an das Management von Bildungseinrichtungen.
Aufgabenstellung
Ich habe bereits eine Visitenkarte, an deren Design sich orientiert werden kann. Ich habe dieses über ein Visitenkarten-Tool erstellen lassen und besitze keine Daten dazu. Ein Foto hänge ich an.

```html
<!DOCTYPE html>
<html lang="de">
<head>
<meta charset="utf-8">
<title>Mara Velten – Qualität und Nachhaltigkeit in der Bildung</title>
<link rel="stylesheet" href="https://fonts.googleapis.com/css2?family=Lato:ital,wght@0,300;0,400;0,700;0,900;1,400&family=Playfair+Display:ital,wght@1,600&display=swap">
<style>
:root{
  --navy:#0b3d6b;
  --hero-deep:#0c3562;
  --hero-mid:#1a5590;
  --green:#8cc63f;
  --ink:#1b1b1b;
  --muted:#5a5a5a;
  --line:#d4d4d4;
  --tab-grey:#6c7377;
  --footer:#f2f2f2;
  --white:#ffffff;
}
*{box-sizing:border-box;margin:0;padding:0}
html,body{width:1200px;height:2385px;overflow:hidden}
body{position:relative;font-family:'Lato',sans-serif;color:var(--ink);background:var(--white)}

/* hero */
.hero{position:absolute;left:0;top:0;width:1200px;height:536px;background:linear-gradient(180deg,#184d84 0%,var(--hero-deep) 60%,#0a2d55 100%)}
.hero-crowd{position:absolute;inset:0;background:radial-gradient(ellipse at 30% 35%,rgba(60,110,170,.55),transparent 60%),radial-gradient(ellipse at 75% 60%,rgba(40,90,150,.5),transparent 55%)}
.hero-portrait{position:absolute;left:792px;top:74px;width:275px;height:462px;background:linear-gradient(180deg,#b8aa9c 0%,#8d8c90 45%,#6f7278 100%);border-radius:110px 110px 0 0}
.logo-ring{position:absolute;width:78px;height:78px;border:3px solid var(--white);border-radius:50%;display:flex;align-items:center;justify-content:center;font-weight:900;font-size:11px;letter-spacing:-.2px;color:var(--white);text-align:center;line-height:1}
.nav{position:absolute;top:33px;left:0;font-size:13px;color:var(--white)}
.nav a{position:absolute;white-space:nowrap;color:var(--white);text-decoration:none}
.nav .active::after{content:"";position:absolute;left:-10px;right:-20px;top:30px;height:2px;background:var(--green)}
.call-top{position:absolute;left:878px;top:22px;width:172px;height:35px;background:var(--green);border-radius:2px;display:flex;align-items:center;justify-content:center;gap:8px;font-size:14px;color:var(--ink)}
.hero-name{position:absolute;left:143px;top:140px;font-family:'Playfair Display',serif;font-style:italic;font-weight:600;font-size:140px;line-height:1;color:var(--white);transform:scaleX(.56);transform-origin:left top;white-space:nowrap;letter-spacing:2px}
.hero-topics{position:absolute;left:148px;top:270px;font-weight:300;font-size:45px;line-height:56px;color:var(--white)}
.hero-band{position:absolute;left:150px;top:382px;width:541px;height:32px;background:#0b1a2c;color:var(--white);font-size:13.5px;letter-spacing:.9px;display:flex;align-items:center;justify-content:center}
.call-hero{position:absolute;left:150px;top:435px;width:220px;height:44px;background:#d9dee5;border:1px solid #fff;border-radius:2px;display:flex;align-items:center;justify-content:center;gap:12px;font-weight:700;font-size:17px;color:var(--hero-deep)}

/* about */
.about-title{position:absolute;left:0;width:1200px;top:592px;text-align:center;font-weight:900;font-size:49px;color:var(--navy)}
.about-lead{position:absolute;left:221px;top:662px;width:758px;font-style:italic;font-size:15px;line-height:23px;text-align:justify}
.tab{position:absolute;top:734px;height:37px;color:var(--white);font-size:14px;font-weight:700;display:flex;align-items:center;justify-content:center;border-radius:2px 2px 0 0}
.tab-active{left:227px;width:184px;background:var(--navy)}
.tab-idle{left:421px;width:185px;background:var(--tab-grey);font-weight:400}
.career{position:absolute;left:218px;top:771px;width:764px;height:533px;border:1px solid var(--line);border-radius:2px}
.job{position:absolute;font-size:12.5px;line-height:1.25}
.job .period{display:block}
.job .role{display:block;margin-top:6px;color:var(--navy);font-weight:700;font-size:14.5px}
.job .org{display:block;margin-top:7px}
.job-current .desc{display:block;margin-top:25px;width:680px;line-height:19.5px}
.partner-badge{position:absolute;left:491px;top:994px;width:92px;height:44px;border:1px solid var(--line);background:#fafafa}
.divider{position:absolute;left:252px;width:697px;height:1px;background:var(--line)}

/* services */
.services{position:absolute;left:0;top:1368px;width:1200px;height:544px;background:linear-gradient(90deg,#8b8a86 0%,#a8a49d 25%,#b7b2aa 60%,#a9a59f 100%)}
.services-portrait{position:absolute;left:210px;top:0;width:230px;height:544px;background:linear-gradient(180deg,#a68f80 0%,#3b3b3d 45%,#262628 100%);border-radius:100px 100px 0 0;opacity:.9}
.services-title{position:absolute;left:0;width:1200px;top:88px;text-align:center;font-weight:900;font-size:49px;color:var(--navy)}
.services-band{position:absolute;left:330px;top:151px;width:537px;height:30px;background:rgba(240,240,240,.92);font-size:15.5px;display:flex;align-items:center;justify-content:center}
.card{position:absolute;top:208px;width:213px;height:286px;background:var(--white)}
.card-visual{height:144px}
.card h3{margin:18px 20px 0 20px;font-size:14.5px;font-weight:700;color:var(--navy);line-height:17px}
.card p{margin:9px 20px 0 22px;font-size:11px;line-height:15.8px;color:#333}
.card .more{position:absolute;left:25px;bottom:14px;font-size:11px;font-weight:700;color:#333}

/* contact */
.contact-logo{position:absolute;left:204px;top:1983px;width:78px;height:78px;border:3px solid #1b1b1b;border-radius:50%;display:flex;align-items:center;justify-content:center;font-weight:900;font-size:11px;line-height:1;text-align:center}
.contact-line{position:absolute;left:204px;display:flex;align-items:center;gap:10px;font-size:13px;color:#444}
.field{position:absolute;border:1px solid var(--line);font-size:11px;color:#8a8a8a;padding:10px 17px;background:var(--white)}
.send{position:absolute;left:794px;top:2181px;width:255px;height:38px;background:var(--green);color:var(--white);font-weight:700;font-size:15px;letter-spacing:.5px;display:flex;align-items:center;justify-content:center;gap:10px}

/* footer */
.footer{position:absolute;left:0;top:2303px;width:1200px;height:82px;background:var(--footer)}
.footer-copy{position:absolute;left:149px;top:30px;font-size:12.5px;color:#666}
.social-dot{position:absolute;top:32px;width:14px;height:14px;border:1.6px solid #333;border-radius:50%}
</style>
</head>
<body>

<header class="hero">
  <div class="hero-crowd" role="img" aria-label="Blau getöntes Foto einer großen Gruppe lächelnder Menschen"></div>
  <div class="hero-portrait" role="img" aria-label="Porträtfoto der Beraterin mit verschränkten Armen im grauen Blazer"></div>
  <div class="logo-ring" style="left:151px;top:5px">MARA<br>VELTEN</div>
  <nav class="nav">
    <a class="active" style="left:529px">Über mich</a>
    <a style="left:630px">Meine Leistungen</a>
    <a style="left:771px">Kontakt</a>
  </nav>
  <div class="call-top">
    <svg width="15" height="15" viewBox="0 0 24 24" fill="none" stroke="#1b1b1b" stroke-width="1.8"><path d="M5 3h4l2 5-3 2a11 11 0 0 0 6 6l2-3 5 2v4a2 2 0 0 1-2 2A17 17 0 0 1 3 5a2 2 0 0 1 2-2z"/><path d="M14 3a7 7 0 0 1 7 7M14 7a3 3 0 0 1 3 3"/></svg>
    +49 151 2048 7731
  </div>
  <h1 class="hero-name">MARA VELTEN</h1>
  <p class="hero-topics">EFQM, Qualitätsmanagement,<br>Nachhaltigkeitsmanagement</p>
  <div class="hero-band">für Volkshochschulen und andere Institutionen der Erwachsenenbildung</div>
  <div class="call-hero">
    <svg width="20" height="20" viewBox="0 0 24 24" fill="none" stroke="#0c3562" stroke-width="1.8"><path d="M5 3h4l2 5-3 2a11 11 0 0 0 6 6l2-3 5 2v4a2 2 0 0 1-2 2A17 17 0 0 1 3 5a2 2 0 0 1 2-2z"/><path d="M14 3a7 7 0 0 1 7 7M14 7a3 3 0 0 1 3 3"/></svg>
    +49 151 2048 7731
  </div>
</header>

<section>
  <h2 class="about-title">Über mich</h2>
  <p class="about-lead">Selbstständig, Verantwortlich Ressourcen schonen - Beratung zu Nachhaltigkeit &amp; Qualität, Mara Velten - Qualität und Nachhaltigkeit in der Bildung</p>
  <div class="tab tab-active">Professional experience</div>
  <div class="tab tab-idle">Educational background</div>
  <div class="career"></div>

  <div class="job job-current" style="left:261px;top:807px">
    <span class="period"><b>Current</b> 8 months, since May 2022</span>
    <span class="role">Verantwortlich Ressourcen schonen - Beratung zu Nachhaltigkeit &amp; Qualität</span>
    <span class="org">Mara Velten - Qualität und Nachhaltigkeit in der Bildung</span>
    <span class="desc">Volkshochschulen und andere Bildungsinstitutionen sichern unsere Zukunft. Auch indem sie verantwortlich mit Energie und anderen Ressourcen umgehen. Ich unterstütze dabei, eine qualitätsgesicherte Nachhaltigkeit praktisch umzusetzen und damit lehrend und Beispiel gebend voranzugehen.</span>
  </div>

  <div class="job" style="left:262px;top:989px">
    <span class="period">8 months, Mar 2021 - Oct 2021</span>
    <span class="role">Leiterin Mehrgenerationenhaus</span>
    <span class="org">Stadt Bergstetten</span>
  </div>
  <div class="partner-badge" role="img" aria-label="Badge des Arbeitgebers"></div>
  <div class="job" style="left:677px;top:989px">
    <span class="period">10 years and 5 months, Oct 2010 - Feb 2021</span>
    <span class="role">Geschäftsführerin</span>
    <span class="org">Volkshochschule Talbrunn e.V.</span>
  </div>
  <div class="divider" style="top:1073px"></div>

  <div class="job" style="left:267px;top:1086px">
    <span class="period">7 years and 7 months, Mar 2003 - Sep 2010</span>
    <span class="role">Dozentin für Betriebswirtschaft und Marketing</span>
    <span class="org">Lernwerk Rainau</span>
  </div>
  <div class="job" style="left:677px;top:1086px">
    <span class="period">1 year and 9 months, Feb 2001 - Oct 2002</span>
    <span class="role">Communication Managerin E-Commerce</span>
    <span class="org">Kravik AG, Steinau, Liechtenstein</span>
  </div>
  <div class="divider" style="top:1170px"></div>

  <div class="job" style="left:267px;top:1183px">
    <span class="period">2 years and 9 months, Apr 1998 - Dec 2000</span>
    <span class="role">Assistenz der Verkaufsleitung</span>
    <span class="org">FELDMANN Vertriebs GmbH</span>
  </div>
  <div class="job" style="left:677px;top:1183px">
    <span class="period">6 months, Oct 1997 - Mar 1998</span>
    <span class="role">Assistenz der Geschäftsführung</span>
    <span class="org">FELDMANN Vertriebs GmbH</span>
  </div>
</section>

<section class="services" role="img" aria-label="Foto der Beraterin vor einer grauen Holz- und Betonwand">
  <div class="services-portrait"></div>
  <h2 class="services-title">Meine Leistungen</h2>
  <div class="services-band">Verantwortlich Ressourcen schonen - Beratung zu Nachhaltigkeit &amp; Qualität</div>

  <article class="card" style="left:151px">
    <div class="card-visual" role="img" aria-label="Skizze von Diagrammen auf weißer Wand" style="background:linear-gradient(135deg,#f3f3f3,#dfe3e8)"></div>
    <h3>EFQM</h3>
    <p>Lorem ipsum dolor sit amet, consectetur adipiscing elit, sed do eiusmod tempor incididunt ut labore et dolore magna aliqua.</p>
    <span class="more">Mehr....</span>
  </article>
  <article class="card" style="left:380px">
    <div class="card-visual" role="img" aria-label="Hand mit leuchtenden goldenen Sternen" style="background:radial-gradient(circle at 50% 35%,#c9a53a,#1d4a63 65%,#0e2a3a)"></div>
    <h3>Qualitätsmanagement</h3>
    <p>Lorem ipsum dolor sit amet, consectetur adipiscing elit, sed do eiusmod tempor incididunt ut labore et dolore magna aliqua.</p>
    <span class="more">Mehr....</span>
  </article>
  <article class="card" style="left:607px">
    <div class="card-visual" role="img" aria-label="Hände halten eine gläserne Erdkugel mit Baum" style="background:linear-gradient(180deg,#7fb43c,#3e7a2a 70%,#c9b79c)"></div>
    <h3>Nachhaltigkeitsmanagement</h3>
    <p>Lorem ipsum dolor sit amet, consectetur adipiscing elit, sed do eiusmod tempor...</p>
    <span class="more">Mehr....</span>
  </article>
  <article class="card" style="left:836px">
    <div class="card-visual" role="img" aria-label="Vortragssaal mit Tischreihen" style="background:linear-gradient(180deg,#cfc9c2,#8b7a6a 60%,#5a4f47)"></div>
    <h3>Für Volkshochschulen und andere Institutionen der Erwachsenenbildung</h3>
    <p>Lorem ipsum dolor sit amet, consectetur adipiscing elit, sed...</p>
    <span class="more">Mehr....</span>
  </article>
</section>

<section>
  <div class="contact-logo">MARA<br>VELTEN</div>
  <div class="contact-line" style="top:2081px">
    <svg width="16" height="16" viewBox="0 0 24 24" fill="none" stroke="#333" stroke-width="1.6"><path d="M22 2L2 10l8 3 3 9z"/><path d="M22 2L10 13"/></svg>
    info@velten-beratung.de
  </div>
  <div class="contact-line" style="top:2111px">
    <svg width="16" height="16" viewBox="0 0 24 24" fill="none" stroke="#333" stroke-width="1.6"><path d="M5 3h4l2 5-3 2a11 11 0 0 0 6 6l2-3 5 2v4a2 2 0 0 1-2 2A17 17 0 0 1 3 5a2 2 0 0 1 2-2z"/></svg>
    +49 151 2048 7731
  </div>
  <div class="contact-line" style="top:2147px;gap:8px">
    <svg width="14" height="18" viewBox="0 0 14 18"><path d="M7 0a7 7 0 0 0-7 7c0 5 7 11 7 11s7-6 7-11a7 7 0 0 0-7-7zm0 10a3 3 0 1 1 0-6 3 3 0 0 1 0 6z" fill="#1b1b1b"/></svg>
    Bergstetten, Germany
  </div>

  <div class="field" style="left:523px;top:1994px;width:253px;height:38px">Vorname</div>
  <div class="field" style="left:794px;top:1994px;width:255px;height:38px">Nachname</div>
  <div class="field" style="left:523px;top:2046px;width:253px;height:38px">Email</div>
  <div class="field" style="left:794px;top:2046px;width:255px;height:38px">Telefon</div>
  <div class="field" style="left:523px;top:2099px;width:526px;height:68px">Kommentare</div>
  <div class="send">
    <svg width="16" height="16" viewBox="0 0 24 24" fill="none" stroke="#fff" stroke-width="1.8"><path d="M22 2L2 10l8 3 3 9z"/><path d="M22 2L10 13"/></svg>
    SENDEN
  </div>
</section>

<footer class="footer">
  <span class="footer-copy">@2022. velten-beratung.de</span>
  <span class="social-dot" style="left:969px"></span>
  <span class="social-dot" style="left:1001px"></span>
  <span class="social-dot" style="left:1035px"></span>
</footer>

</body>
</html>
```